Debt Reduction Visuals

I need two images created for screens not print. My intent is to use simple imagery to communicate how paying down debt can make a huge impact on our church. I want to use simple "icon" style images, clean lines, soothing colors (blues, grays. oranges) and a very legible font.

```html
<!DOCTYPE html>
<html lang="en">
<head>
<meta charset="utf-8">
<title>Debt Reduction Visuals</title>
<link href="https://fonts.googleapis.com/css2?family=Montserrat:wght@800&display=swap" rel="stylesheet">
<style>
  :root {
    --page-top: #e9eaec;
    --page-bottom: #f6f6f6;
    --navy-deep: #03073f;
    --navy-mid: #041a86;
    --blue-bright: #0b4ccc;
    --white: #ffffff;
    --orange: #fb9019;
    --orange-light: #ffc58e;
    --orange-tag: #f38b3b;
    --gold: #e8c128;
    --gold-light: #efdfa8;
    --gray: #888888;
    --gray-light: #d3d4d6;
    --teal: #00b0ab;
    --teal-light: #bde7e5;
  }
  html, body {
    margin: 0;
    width: 1024px;
    height: 1200px;
    overflow: hidden;
  }
  body {
    position: relative;
    background: linear-gradient(180deg, var(--page-top), var(--page-bottom));
    font-family: "Montserrat", Arial, sans-serif;
  }
  .visual {
    position: absolute;
    left: 127px;
    width: 770px;
    height: 433px;
    background:
      linear-gradient(145deg, transparent 55%, rgba(255,255,255,0.05) 55%, rgba(255,255,255,0.05) 70%, transparent 70%),
      linear-gradient(145deg, transparent 30%, rgba(0,0,0,0.08) 30%, rgba(0,0,0,0.08) 45%, transparent 45%),
      linear-gradient(35deg, var(--navy-deep) 0%, var(--navy-mid) 50%, var(--blue-bright) 100%);
    box-shadow: 10px 18px 22px rgba(0,0,0,0.35);
  }
  .visual--payments { top: 80px; }
  .visual--impact { top: 683px; }
  .visual svg { display: block; }
  .tag-text {
    font-family: "Montserrat", Arial, sans-serif;
    font-weight: 800;
    font-size: 19px;
    fill: var(--white);
    letter-spacing: 0.3px;
  }
  .icon-line {
    fill: none;
    stroke: var(--white);
    stroke-width: 11;
    stroke-linejoin: miter;
  }
</style>
</head>
<body>

<section class="visual visual--payments" aria-label="Church payments to the bank">
  <svg width="770" height="433" viewBox="0 0 770 433">
    <defs>
      <filter id="soft-shadow" x="-30%" y="-30%" width="160%" height="160%">
        <feDropShadow dx="0" dy="3" stdDeviation="5" flood-color="#000" flood-opacity="0.35"/>
      </filter>
      <clipPath id="church-disc-a"><circle cx="180" cy="174" r="103"/></clipPath>
      <clipPath id="bank-disc"><circle cx="557" cy="209" r="130"/></clipPath>
    </defs>

    <!-- flow arrow -->
    <path class="flow-arrow" d="M281 56 L361 52 L403 83 L398 71 L417 104 L381 100 L392 95 L357 69 L282 73 Z" fill="var(--white)"/>

    <!-- church marker -->
    <g class="church-marker" filter="url(#soft-shadow)">
      <circle cx="180" cy="174" r="116" fill="var(--white)"/>
      <path d="M163 286 L180 313 L197 286 Z" fill="var(--white)"/>
    </g>
    <g clip-path="url(#church-disc-a)">
      <circle cx="180" cy="174" r="103" fill="var(--orange-light)"/>
      <ellipse cx="180" cy="153" rx="106" ry="104" fill="var(--orange)"/>
    </g>
    <path d="M171 283 L180 297 L189 283 Z" fill="var(--orange-light)"/>
    <g class="icon-church" transform="translate(180 174) scale(0.579) translate(-530 -440)">
      <path class="icon-line" d="M530 322 V372 M515 337 H545"/>
      <path class="icon-line" d="M437 437 L530 373 L624 437"/>
      <path class="icon-line" d="M462 522 V447 L530 398 L598 447 V522"/>
      <path class="icon-line" d="M424 528 V480 L462 458 M598 458 L636 480 V528"/>
      <path class="icon-line" d="M420 528 H640"/>
      <path class="icon-line" d="M510 522 V482 A20 20 0 0 1 550 482 V522"/>
    </g>

    <!-- bank marker -->
    <circle cx="557" cy="209" r="147" fill="var(--white)" filter="url(#soft-shadow)"/>
    <g clip-path="url(#bank-disc)">
      <circle cx="557" cy="209" r="130" fill="var(--gray-light)"/>
      <ellipse cx="557" cy="183" rx="132" ry="117" fill="var(--gray)"/>
    </g>
    <g class="icon-bank" transform="translate(557 209) scale(0.579) translate(-1181 -500)">
      <path class="icon-line" stroke-width="8" d="M1064 430 L1181 382 L1298 430 V445 H1064 Z"/>
      <path class="icon-line" stroke-width="8" d="M1098 430 H1264"/>
      <path class="icon-line" stroke-width="8" d="M1076 452 H1286 V464 H1076 Z"/>
      <path class="icon-line" stroke-width="8" d="M1082 464 V578 M1280 464 V578"/>
      <path class="icon-line" stroke-width="8" d="M1108 478 V560 M1133 468 V574 M1158 468 V500 M1204 468 V500 M1229 468 V574 M1254 478 V560 M1158 540 V574 M1204 540 V574"/>
      <circle cx="1181" cy="518" r="35" fill="none" stroke="var(--white)" stroke-width="8"/>
      <path class="icon-line" stroke-width="6" d="M1195 504 Q1181 494 1170 504 Q1164 514 1181 518 Q1198 522 1192 533 Q1181 542 1166 532 M1181 492 V500 M1181 536 V544"/>
      <path class="icon-line" stroke-width="8" d="M1076 578 H1286 V592 H1076 Z"/>
      <path class="icon-line" stroke-width="8" d="M1064 598 H1298 V616 H1064 Z"/>
    </g>

    <!-- amounts -->
    <g class="amount-tag">
      <rect x="86" y="320" width="30" height="28" fill="var(--orange-tag)"/>
      <rect x="110" y="320" width="6" height="28" fill="var(--orange-light)"/>
      <rect x="117" y="321" width="221" height="26" fill="none" stroke="var(--white)" stroke-width="2"/>
      <text class="tag-text" x="135" y="342">$60,000 WEEKLY</text>
    </g>
    <g class="amount-tag">
      <rect x="86" y="358" width="30" height="28" fill="var(--orange-tag)"/>
      <rect x="110" y="358" width="6" height="28" fill="var(--orange-light)"/>
      <rect x="117" y="359" width="259" height="26" fill="none" stroke="var(--white)" stroke-width="2"/>
      <text class="tag-text" x="135" y="380">$726,000 ANNUALLY</text>
    </g>
  </svg>
</section>

<section class="visual visual--impact" aria-label="Church savings for the community">
  <svg width="770" height="433" viewBox="0 0 770 433">
    <defs>
      <filter id="soft-shadow-b" x="-30%" y="-30%" width="160%" height="160%">
        <feDropShadow dx="0" dy="3" stdDeviation="5" flood-color="#000" flood-opacity="0.35"/>
      </filter>
      <clipPath id="church-disc-b"><circle cx="180" cy="174" r="103"/></clipPath>
      <clipPath id="people-disc"><circle cx="557" cy="209" r="130"/></clipPath>
    </defs>

    <path class="flow-arrow" d="M281 56 L361 52 L403 83 L398 71 L417 104 L381 100 L392 95 L357 69 L282 73 Z" fill="var(--white)"/>

    <g class="church-marker" filter="url(#soft-shadow-b)">
      <circle cx="180" cy="174" r="116" fill="var(--white)"/>
      <path d="M163 286 L180 313 L197 286 Z" fill="var(--white)"/>
    </g>
    <g clip-path="url(#church-disc-b)">
      <circle cx="180" cy="174" r="103" fill="var(--gold-light)"/>
      <ellipse cx="180" cy="153" rx="106" ry="104" fill="var(--gold)"/>
    </g>
    <path d="M171 283 L180 297 L189 283 Z" fill="var(--gold-light)"/>
    <g class="icon-church" transform="translate(180 174) scale(0.579) translate(-530 -440)">
      <path class="icon-line" d="M530 322 V372 M515 337 H545"/>
      <path class="icon-line" d="M437 437 L530 373 L624 437"/>
      <path class="icon-line" d="M462 522 V447 L530 398 L598 447 V522"/>
      <path class="icon-line" d="M424 528 V480 L462 458 M598 458 L636 480 V528"/>
      <path class="icon-line" d="M420 528 H640"/>
      <path class="icon-line" d="M510 522 V482 A20 20 0 0 1 550 482 V522"/>
    </g>

    <circle cx="557" cy="209" r="147" fill="var(--white)" filter="url(#soft-shadow-b)"/>
    <g clip-path="url(#people-disc)">
      <circle cx="557" cy="209" r="130" fill="var(--teal-light)"/>
      <ellipse cx="557" cy="183" rx="132" ry="117" fill="var(--teal)"/>
    </g>
    <g class="icon-community" fill="var(--white)" stroke="var(--teal)" stroke-width="5" transform="translate(557 209) scale(0.579) translate(-1181 -1545)">
      <path d="M1036 1620 V1580 Q1036 1555 1060 1555 H1072 Q1096 1555 1096 1580 V1620 Z"/>
      <path d="M1266 1620 V1580 Q1266 1555 1290 1555 H1302 Q1326 1555 1326 1580 V1620 Z"/>
      <circle cx="1064" cy="1527" r="18"/>
      <circle cx="1296" cy="1527" r="18"/>
      <path d="M1072 1640 V1572 Q1072 1535 1108 1535 H1118 Q1150 1535 1150 1572 V1640 Z"/>
      <path d="M1212 1640 V1572 Q1212 1535 1244 1535 H1254 Q1290 1535 1290 1572 V1640 Z"/>
      <circle cx="1112" cy="1505" r="27"/>
      <circle cx="1248" cy="1505" r="27"/>
      <path d="M1124 1662 V1570 Q1124 1512 1181 1512 Q1238 1512 1238 1570 V1662 Z"/>
      <circle cx="1181" cy="1468" r="37"/>
    </g>

    <g class="amount-tag">
      <rect x="72" y="338" width="30" height="28" fill="var(--gold)"/>
      <rect x="96" y="338" width="6" height="28" fill="var(--gold-light)"/>
      <rect x="103" y="339" width="221" height="26" fill="none" stroke="var(--white)" stroke-width="2"/>
      <text class="tag-text" x="121" y="360">$1.4 MILLION</text>
    </g>
  </svg>
</section>

</body>
</html>
```